PTA Meeting Poster

We are looking to create a poster to invite parents of our school to our monthly PTA Meeting.

The copy should include:

PTA Meeting
This Wednesday
8:40am
in the Multi Purpose Room

All Welcome!

```html
<!DOCTYPE html>
<html lang="en">
<head>
<meta charset="utf-8">
<title>PTA Meeting Poster</title>
<link rel="stylesheet" href="https://fonts.googleapis.com/css2?family=Open+Sans:wght@600&family=Roboto+Condensed:wght@400&family=Roboto:wght@700&family=Source+Sans+3:wght@600&family=Urbanist:wght@700&display=swap">
<style>
  :root {
    --bg-dark: #2a0630;
    --bg-mid: #5c1266;
    --bg-bright: #8a1a93;
    --orange: #ffa400;
    --green: #33ff00;
    --cyan: #22e6e6;
    --white: #ffffff;
    --ink: #000000;
  }
  html, body {
    margin: 0;
    padding: 0;
    width: 1200px;
    height: 1200px;
    overflow: hidden;
    background: var(--bg-dark);
  }
  .poster {
    position: relative;
    width: 1200px;
    height: 1200px;
  }
  .poster__texture {
    position: absolute;
    inset: 0;
    background:
      radial-gradient(ellipse at 50% 45%, var(--bg-bright) 0%, var(--bg-mid) 55%, var(--bg-dark) 100%);
  }
  .poster__copy {
    position: absolute;
    inset: 0;
  }
  .title {
    font-family: "Open Sans", sans-serif;
    font-weight: 600;
    font-size: 88px;
    fill: var(--orange);
  }
  .day {
    font-family: "Roboto Condensed", sans-serif;
    font-weight: 400;
    font-size: 60px;
    fill: var(--green);
    stroke: var(--ink);
    stroke-width: 4px;
    paint-order: stroke;
  }
  .time {
    font-family: "Roboto", sans-serif;
    font-weight: 700;
    font-size: 68px;
    fill: var(--cyan);
    stroke: var(--ink);
    stroke-width: 5px;
    paint-order: stroke;
  }
  .venue {
    font-family: "Source Sans 3", sans-serif;
    font-weight: 600;
    font-size: 90px;
    fill: var(--white);
    stroke: var(--ink);
    stroke-width: 8px;
    paint-order: stroke;
  }
  .welcome {
    font-family: "Urbanist", sans-serif;
    font-weight: 700;
    font-size: 110px;
    fill: var(--white);
    stroke: var(--ink);
    stroke-width: 7px;
    paint-order: stroke;
  }
</style>
</head>
<body>
  <main class="poster">
    <div class="poster__texture" role="img" aria-label="Speckled magenta and black textured background"></div>
    <svg class="poster__copy" width="1200" height="1200" viewBox="0 0 1200 1200">
      <text class="title" x="600" y="242" text-anchor="middle" textLength="720" lengthAdjust="spacingAndGlyphs">PTA Meeting</text>
      <text class="day" x="1153" y="363" text-anchor="end" textLength="357" lengthAdjust="spacingAndGlyphs">This Wednesday</text>
      <text class="time" x="1155" y="437" text-anchor="end" textLength="352" lengthAdjust="spacingAndGlyphs">8:40am</text>
      <text class="venue" x="615" y="622" text-anchor="middle" textLength="1070" lengthAdjust="spacingAndGlyphs">in the Multi Purpose Room</text>
      <text class="welcome" x="611" y="917" text-anchor="middle" textLength="795" lengthAdjust="spacingAndGlyphs">All Welcome!</text>
    </svg>
  </main>
</body>
</html>
```